Bring my website out of the dark ages!

Website redesign for Velmar Consulting
www.velmarqx.com and www.trundlebox.ca
Currently dark (black), small font, boring, old
Want something simple, bright, fun, modern, clean and professional
Flexible content, any ideas appreciated
In business since 1998, focused on long term client relationships and being there when it matters.
Specialize solutions for clients based on their needs, vision and budget, not what the IT market thinks is the latest and greatest (and most profitable).
Want to eventually add helpful content (videos) and testimonials to the site for the benefit of the visitor

Target Market(s)

Anyone looking for IT services - target is a business with 25-100 employees.

Industry/Entity Type

It Company

Coding

Coded - Design and coding required

Number of Pages Required

4 page

Colors

Designer to choose colors to be used in the design.

Requirements
Must have
• Bright, clean, simple, no scrolling, fast
Nice to have
• Neat animation of some kind
Should not have
• scrolling
• too much information

```html
<!DOCTYPE html>
<html lang="en">
<head>
<meta charset="utf-8">
<title>Velmar Consulting — Your Partner in Technology Solutions</title>
<link rel="stylesheet" href="https://fonts.googleapis.com/css2?family=Poppins:wght@300;400&display=swap">
<style>
  :root {
    --ink: #ffffff;
    --accent: #f7a81b;
    --shade: rgba(18, 22, 30, 0.34);
    --photo-light: #eef1f4;
    --photo-mid: #b9c2cb;
    --photo-warm: #d9b48c;
    --photo-deep: #3b4656;
  }
  * { box-sizing: border-box; margin: 0; padding: 0; }
  html, body { width: 1200px; height: 677px; overflow: hidden; background: #8a94a0; }
  body { font-family: "Poppins", sans-serif; font-weight: 300; color: var(--ink); }

  .hero { position: relative; width: 1200px; height: 677px; overflow: hidden; }
  .hero-photo {
    position: absolute; inset: 0;
    background:
      radial-gradient(ellipse 45% 55% at 32% 30%, var(--photo-light) 0%, transparent 70%),
      radial-gradient(ellipse 30% 40% at 30% 55%, var(--photo-warm) 0%, transparent 70%),
      radial-gradient(ellipse 35% 50% at 68% 62%, var(--photo-deep) 0%, transparent 75%),
      radial-gradient(ellipse 25% 60% at 98% 70%, var(--photo-deep) 0%, transparent 75%),
      linear-gradient(115deg, var(--photo-mid) 0%, #d7dde3 45%, #9aa6b3 100%);
  }
  .hero-shade { position: absolute; inset: 0; background: var(--shade); }

  .site-header {
    position: absolute; top: 0; left: 0; right: 0; height: 110px;
    display: flex; align-items: center; padding: 0 52px;
  }
  .brand { font-size: 21px; font-weight: 300; letter-spacing: 0.5px; color: var(--ink); width: 258px; white-space: nowrap; }
  .main-nav { display: flex; gap: 31px; font-size: 17.5px; }
  .main-nav a { color: var(--ink); text-decoration: none; letter-spacing: 0.3px; }
  .main-nav a.is-active { color: var(--accent); }
  .header-phone {
    margin-left: auto; display: flex; align-items: center; gap: 18px;
    font-size: 23px; letter-spacing: 1px;
  }
  .header-phone svg { width: 19px; height: 19px; fill: var(--ink); }

  .hero-content {
    position: absolute; top: 255px; left: 0; right: 0; text-align: center;
    text-shadow: 0 1px 12px rgba(0, 0, 0, 0.25);
  }
  .hero-title { font-size: 43px; font-weight: 300; line-height: 60px; letter-spacing: 0.5px; }
  .hero-link {
    display: inline-flex; align-items: center; gap: 20px; margin-top: 34px;
    color: var(--accent); font-size: 17.5px; font-weight: 400; letter-spacing: 1px; text-decoration: none;
  }
  .hero-link svg { width: 20px; height: 12px; }

  .social-list {
    position: absolute; top: 586px; left: 0; right: 0;
    display: flex; justify-content: center; gap: 12px; list-style: none;
  }
  .social-list li {
    width: 42px; height: 42px; border: 1.5px solid var(--ink); border-radius: 50%;
    display: flex; align-items: center; justify-content: center;
  }
  .social-dot { width: 10px; height: 10px; border-radius: 50%; background: var(--ink); }
</style>
</head>
<body>
<section class="hero">
  <div class="hero-photo" role="img" aria-label="Photo of a business team in a bright office meeting around a table with a laptop, tablet and printed charts"></div>
  <div class="hero-shade"></div>

  <header class="site-header">
    <div class="brand">Velmar Consulting</div>
    <nav class="main-nav">
      <a href="#" class="is-active">Home</a>
      <a href="#">About Us</a>
      <a href="#">Services</a>
      <a href="#">Testimonials</a>
      <a href="#">Contact Us</a>
    </nav>
    <div class="header-phone">
      <svg viewBox="0 0 24 24" aria-hidden="true"><path d="M6.6 10.8a15.1 15.1 0 0 0 6.6 6.6l2.2-2.2c.3-.3.7-.4 1-.2 1.1.4 2.3.6 3.6.6.6 0 1 .4 1 1V20c0 .6-.4 1-1 1A17 17 0 0 1 3 4c0-.6.4-1 1-1h3.5c.6 0 1 .4 1 1 0 1.3.2 2.5.6 3.6.1.3 0 .7-.2 1l-2.3 2.2z"/></svg>
      <span>403 555 0142</span>
    </div>
  </header>

  <div class="hero-content">
    <h1 class="hero-title">Your Partner in<br>Technology Solutions</h1>
    <a href="#" class="hero-link">View Details
      <svg viewBox="0 0 20 12" aria-hidden="true"><path d="M0 6h17M12 1l5 5-5 5" stroke="#ffffff" stroke-width="2" fill="none"/></svg>
    </a>
  </div>

  <ul class="social-list" aria-label="Social links">
    <li><span class="social-dot"></span></li>
    <li><span class="social-dot"></span></li>
    <li><span class="social-dot"></span></li>
  </ul>
</section>
</body>
</html>
```